Auto Window Tinting for Local Business
Need Business card design
New card design

Target Market(s)

Local Audience
Repeat clients

Industry/Entity Type

Automotive Part

Contact Information for Business Card

Auto Window Tinting new crd design

Font styles to use
Serif

Colors

Designer to choose colors to be used in the design.

Requirements
Must have
• Facebook address
• IG address
• Phone Number
Nice to have
• Your own ideas
• Bold design
Should not have
• Auto graphics minimal
• Too many bright colors

```html
<!DOCTYPE html>
<html lang="en">
<head>
<meta charset="utf-8">
<title>Apex Window Tinting – Business Card</title>
<link rel="stylesheet" href="https://fonts.googleapis.com/css2?family=Michroma&family=Roboto:wght@400;700&display=swap">
<style>
  :root {
    --bg: #1e1e1e;
    --ink: #111111;
    --metal-hi: #fbfbfb;
    --metal-mid: #d9d9d9;
    --metal-lo: #a9a9a9;
  }
  * { margin: 0; padding: 0; box-sizing: border-box; }
  html, body { width: 1200px; height: 960px; overflow: hidden; background: var(--bg); }
  .canvas {
    width: 1200px; height: 960px;
    display: flex; flex-direction: column; align-items: center; justify-content: center; gap: 34px;
  }
  .card {
    position: relative; width: 760px; height: 434px; overflow: hidden;
    color: var(--ink);
    background:
      repeating-linear-gradient(180deg, rgba(255,255,255,0.10) 0 1px, rgba(0,0,0,0.04) 1px 3px),
      radial-gradient(ellipse 70% 60% at 50% 48%, var(--metal-hi) 0%, var(--metal-mid) 55%, var(--metal-lo) 100%);
    box-shadow: 0 10px 30px rgba(0,0,0,0.6);
  }
  .tagline {
    position: absolute; left: 0; right: 0;
    display: flex; align-items: center; justify-content: center; gap: 12px;
    font-family: 'Michroma', sans-serif; font-size: 16px; font-weight: 700; letter-spacing: 1.5px;
    text-transform: uppercase; white-space: nowrap;
  }
  .tagline .rule { display: block; width: 40px; height: 1.5px; background: var(--ink); }

  /* Front */
  .brand { position: absolute; left: 70px; top: 140px; font-family: 'Roboto', sans-serif; white-space: nowrap; }
  .brand-name { font-size: 46px; font-weight: 700; line-height: 1; letter-spacing: 1px; }
  .brand-sub { font-size: 18px; font-weight: 700; letter-spacing: 3px; text-transform: uppercase; margin-top: 6px; }
  .brand-motto { font-size: 14px; margin-top: 4px; }
  .brand-phone { font-size: 34px; font-weight: 700; margin-top: 4px; letter-spacing: 1px; }
  .benefits { position: absolute; left: 430px; top: 140px; list-style: none; font-family: 'Roboto', sans-serif; font-size: 19px; white-space: nowrap; }
  .benefits li { display: flex; align-items: center; gap: 10px; line-height: 29px; }
  .front .tagline { top: 352px; }

  /* Back */
  .person { position: absolute; right: 408px; top: 180px; text-align: right; white-space: nowrap; }
  .person-name { font-family: 'Michroma', sans-serif; font-size: 24px; font-weight: 700; letter-spacing: 2px; text-transform: uppercase; }
  .person-role { font-family: 'Roboto', sans-serif; font-size: 17px; text-transform: uppercase; margin-top: 4px; }
  .divider { position: absolute; left: 372px; top: 150px; width: 1.5px; height: 118px; background: var(--ink); }
  .contacts { position: absolute; left: 396px; top: 152px; list-style: none; font-family: 'Roboto', sans-serif; font-size: 19px; white-space: nowrap; }
  .contacts li { display: flex; align-items: center; gap: 10px; line-height: 36px; }
  .dot { display: inline-flex; align-items: center; justify-content: center; width: 20px; height: 20px; border-radius: 50%; background: var(--ink); }
  .back .tagline { top: 360px; }
</style>
</head>
<body>
<main class="canvas">
  <section class="card front">
    <div class="brand">
      <div class="brand-name">APEX</div>
      <div class="brand-sub">Window Tinting</div>
      <div class="brand-motto">Don't squint, window tint!</div>
      <div class="brand-phone">555-318-2740</div>
    </div>
    <ul class="benefits">
      <li><svg width="18" height="18" viewBox="0 0 18 18"><rect x="1" y="3" width="13" height="13" fill="none" stroke="#111" stroke-width="1.6"/><path d="M4 9l4 4 9-11" fill="none" stroke="#111" stroke-width="2.4"/></svg>Block Unwanted Heat</li>
      <li><svg width="18" height="18" viewBox="0 0 18 18"><rect x="1" y="3" width="13" height="13" fill="none" stroke="#111" stroke-width="1.6"/><path d="M4 9l4 4 9-11" fill="none" stroke="#111" stroke-width="2.4"/></svg>Protect Skin From UV Rays</li>
      <li><svg width="18" height="18" viewBox="0 0 18 18"><rect x="1" y="3" width="13" height="13" fill="none" stroke="#111" stroke-width="1.6"/><path d="M4 9l4 4 9-11" fill="none" stroke="#111" stroke-width="2.4"/></svg>Protect Interior From Fading</li>
      <li><svg width="18" height="18" viewBox="0 0 18 18"><rect x="1" y="3" width="13" height="13" fill="none" stroke="#111" stroke-width="1.6"/><path d="M4 9l4 4 9-11" fill="none" stroke="#111" stroke-width="2.4"/></svg>Improve Overall Appearance</li>
    </ul>
    <div class="tagline"><span class="rule"></span>Mobile Service - Lifetime Warranty<span class="rule"></span></div>
  </section>

  <section class="card back">
    <div class="person">
      <div class="person-name">Marco Delgado</div>
      <div class="person-role">Owner</div>
    </div>
    <div class="divider"></div>
    <ul class="contacts">
      <li><span class="dot"><svg width="12" height="9" viewBox="0 0 12 9"><rect x="0.5" y="0.5" width="11" height="8" fill="none" stroke="#fff"/><path d="M0.5 0.5l5.5 4.5 5.5-4.5" fill="none" stroke="#fff"/></svg></span>apex_windowtint@mailbox.com</li>
      <li><span class="dot"></span>facebook.com/apexwindowtint</li>
      <li><span class="dot"></span>@apex_windowtinting</li>
    </ul>
    <div class="tagline">Mobile Service - Lifetime Warranty</div>
  </section>
</main>
</body>
</html>
```